New lease of life for a tired Country Pub menu, QLD

I need to refresh my menus with updated prices. The menus need to be A4 (the menus are laminated and handed out over the bar. I'd like to include our logo. I will upload our existing menus as well as the new prices. The design should be humble yet stylish if that's ok, please

Target Market(s)

Locals, travellers and workers

Industry/Entity Type

Hospitality, Quintessential Country pub

Font styles to use
Sans Serif

Colors

Designer to choose colors to be used in the design.

Requirements
Must have
• as we run different menus on different nights
Nice to have
• our logo

```html
<!DOCTYPE html>
<html lang="en">
<head>
<meta charset="utf-8">
<title>Hotel Pemberton – Pizza Menu</title>
<link href="https://fonts.googleapis.com/css2?family=Archivo+Black&family=Cutive+Mono&display=swap" rel="stylesheet">
<style>
  :root {
    --paper: #ffffff;
    --sage: #a9c7b2;
    --panel: #405850;
    --tab: #4e7566;
    --ink-light: #ffffff;
    --ink-dark: #405850;
  }
  * { margin: 0; padding: 0; box-sizing: border-box; }
  html, body { width: 840px; height: 1200px; overflow: hidden; background: var(--paper); }
  .menu {
    position: relative;
    width: 840px;
    height: 1200px;
    overflow: hidden;
    background: linear-gradient(to bottom, var(--paper) 0 575px, var(--sage) 575px 100%);
    font-family: "Cutive Mono", monospace;
    color: var(--ink-light);
  }
  .menu-panel {
    position: absolute;
    left: 25px; top: 96px;
    width: 780px; height: 1027px;
    background: var(--panel);
    border-radius: 42px;
  }
  .title-tab {
    position: absolute;
    left: 288px; top: 25px;
    width: 580px; height: 129px;
    background: var(--tab);
    border-radius: 33px 0 0 33px;
  }
  .title {
    position: absolute;
    left: 338px; top: 44px;
    font-family: "Archivo Black", sans-serif;
    font-size: 53px;
    line-height: 60px;
    font-weight: 400;
    letter-spacing: 0.3px;
  }
  .service {
    position: absolute;
    left: 342px; top: 114px;
    font-family: "Archivo Black", sans-serif;
    font-size: 20px;
    line-height: 28px;
    white-space: nowrap;
  }
  .service-days {
    font-family: "Cutive Mono", monospace;
    font-size: 16px;
    letter-spacing: 1.5px;
    margin-left: 8px;
  }
  .brand-name {
    position: absolute;
    left: 40px; top: 48px;
    font-family: "Archivo Black", sans-serif;
    font-size: 20px;
    line-height: 26px;
    font-weight: 400;
    color: var(--ink-dark);
    white-space: nowrap;
  }
  .price-heading {
    position: absolute;
    left: 670px; top: 208px;
    font-family: "Archivo Black", sans-serif;
    font-size: 16px;
    line-height: 22px;
  }
  .pizza {
    position: absolute;
    left: 68px;
    width: 720px;
    top: var(--top);
  }
  .pizza-name {
    font-family: "Archivo Black", sans-serif;
    font-size: 19.5px;
    line-height: 26px;
    font-weight: 400;
    letter-spacing: 0.2px;
  }
  .pizza-toppings {
    margin-top: var(--gap);
    white-space: nowrap;
    font-size: 14.5px;
    line-height: 25px;
    letter-spacing: 0.85px;
  }
  .price {
    position: absolute;
    top: var(--price-top);
    font-size: 14.5px;
    line-height: 25px;
    letter-spacing: 0.85px;
  }
  .price-standard { left: 483px; }
  .price-member { left: 616px; }
  .price-member.short { left: 636px; }
  .footnote {
    position: absolute;
    left: 0; right: 0; top: 1144px;
    text-align: center;
    font-family: "Archivo Black", sans-serif;
    font-size: 20px;
    line-height: 26px;
    color: var(--ink-dark);
  }
</style>
</head>
<body>
<main class="menu">
  <div class="menu-panel"></div>
  <div class="title-tab"></div>

  <p class="brand-name">HOTEL PEMBERTON</p>

  <h1 class="title">PIZZA MENU</h1>
  <p class="service">LUNCH &amp; DINNER<span class="service-days">WEDNESDAYS ONLY</span></p>

  <p class="price-heading">Members</p>

  <section class="pizza" style="--top:237px; --gap:2px; --price-top:41px;">
    <h2 class="pizza-name">HAWAIIAN</h2>
    <p class="pizza-toppings">Tomato sauce, cheddar cheese, Hadley’s<br>smoked ham and pineapple, mozzarella</p>
    <span class="price price-standard">$19.99</span>
    <span class="price price-member">$18.99</span>
  </section>

  <section class="pizza" style="--top:349px; --gap:8px; --price-top:35px;">
    <h2 class="pizza-name">MEAT LOVERS</h2>
    <p class="pizza-toppings">BBQ sauce, cheddar cheese, seasoned mince,<br>Hadley’s smoked ham, beef sausage, mozzarella</p>
    <span class="price price-standard">$19.99</span>
    <span class="price price-member">$18.99</span>
  </section>

  <section class="pizza" style="--top:481px; --gap:4px; --price-top:43px;">
    <h2 class="pizza-name">BBQ SWEET CHILLI CHICKEN</h2>
    <p class="pizza-toppings">BBQ sauce with sweet chili sauce, cheddar<br>cheese, mushrooms, onion, chicken, mozzarella</p>
    <span class="price price-standard">$21</span>
    <span class="price price-member short">$19</span>
  </section>

  <section class="pizza" style="--top:606px; --gap:11px; --price-top:38px;">
    <h2 class="pizza-name">SUPREME</h2>
    <p class="pizza-toppings">Tomato sauce, cheddar cheese, Hadley’s smoked<br>ham, onion, capsicum, mushroom, pepperoni,<br>pineapple, mozzarella olives</p>
    <span class="price price-standard">$18.99</span>
    <span class="price price-member">$17.99</span>
  </section>

  <section class="pizza" style="--top:763px; --gap:12px;">
    <h2 class="pizza-name">VEGETARIAN</h2>
    <p class="pizza-toppings">Tomato sauce, cheddar cheese, onion, mushroom,<br>capsicum, olives, pumpkin</p>
  </section>

  <section class="pizza" style="--top:894px; --gap:11px;">
    <h2 class="pizza-name">PEPPERONI</h2>
    <p class="pizza-toppings">Tomato sauce, cheddar cheese, pepperoni</p>
  </section>

  <section class="pizza" style="--top:1004px; --gap:14px;">
    <h2 class="pizza-name">TANDOORI CHICKEN</h2>
    <p class="pizza-toppings">Tomato/tandoori sauce, cheddar cheese,<br>chicken, onion, capsicum, mozzarella</p>
  </section>

  <p class="footnote">HALF/HALF NOT AVAILABLE</p>
</main>
</body>
</html>
```